Supplement Company looking for product design on a pre-work out and capsule supplement!

We are a small health supplement company that is making health supplements for competitive runners who are looking to increase their endurance. We have the utmost confidence in your ability to produce the best result. The designs sought are for our Pre-Workout supplement called "Kestro Surge-Up" that will be in a 12 oz plastic jar that comes in a and a Sodium Phosphate capsules called "Kestro VX" that will be in a bottle that holds 75 small capsules. We are looking for an amazing design for these products that is simple, and to the point. There are a lot of examples of different products that you can search such as Torvane Strak7, Z9 Pre-workout, UltrA-Sol Multivitamin, and Quillfen Nutrition products.
We do not have a photo of the product because we are looking for your design abilities to make the packaging design come to life on the product. The products should have the same design, same base color (silver), and the individual product colors (Green for Surge-Up and the Turquoise for SP).

Target Market(s)

Competitive Runners

Industry/Entity Type

Health And Wellness

Colors
ffffff
9bcb3c
87cfc6

Requirements
Must have
• A design of each product as to how it would appear in person. Including "Kestro Surge-Up" for the pre-workout and "Kestro VX" for the pills
• Must say "Dietary Supplement," in small print to the bottom left and "Zero banned substances" next to it.
• "Miles of energy, focus, and endurance" for the pre-workout or something to that effect (We are interested to see what else could be supplemented (no pun intended) in place of the word mix).
• The, "KL" from the logo uploaded in somewhere on the top left of the corner of the product.
Nice to have
• Transparent background, product only image that would allow the product to standout and the background on a website to stand without interference.
Should not have
• Colors outside of silver and whatever product color that is designated.

```html
<!DOCTYPE html>
<html lang="en">
<head>
<meta charset="UTF-8">
<title>Kestro Surge-Up Label</title>
<link href="https://fonts.googleapis.com/css2?family=Montserrat:wght@500;600;700;800;900&display=swap" rel="stylesheet">
<style>
  :root {
    --green: #0a8f3f;
    --green-deep: #067a34;
    --lime: #9bcb3c;
    --lime-soft: #c5e27f;
    --charcoal: #2f3336;
    --silver-light: #ffffff;
    --silver-mid: #e6e8e8;
    --silver-dark: #c9cccc;
    --white: #ffffff;
    --page: #ffffff;
  }
  * { margin: 0; padding: 0; box-sizing: border-box; }
  html, body {
    width: 1200px; height: 1200px; overflow: hidden;
    background: var(--page);
    font-family: "Montserrat", Arial, sans-serif;
  }
  .label {
    position: absolute; left: 50px; top: 110px;
    width: 1100px; height: 984px;
    overflow: hidden;
  }
  .label-shapes { position: absolute; inset: 0; }
  .brand-mark {
    position: absolute; left: 22px; top: 100px;
    color: var(--white); font-weight: 800; font-size: 96px;
    letter-spacing: 2px; line-height: 1;
  }
  .claims-note {
    position: absolute; left: 614px; top: 100px;
    color: var(--green); font-weight: 500; font-size: 18px;
  }
  .hero-art {
    position: absolute; left: 380px; top: 55px; width: 560px; height: 400px;
  }
  .spec-line {
    position: absolute; top: 470px;
    color: var(--green); font-weight: 700; font-size: 21px;
  }
  .spec-banned { left: 280px; }
  .spec-weight { left: 706px; font-weight: 600; }
  .spec-weight b { font-weight: 800; margin-left: 14px; }
  .product-name {
    position: absolute; left: 218px; top: 508px;
    color: var(--green); font-weight: 900; font-size: 112px;
    letter-spacing: 2px; line-height: 1;
  }
  .product-variant {
    position: absolute; left: 876px; top: 520px;
    width: 160px; height: 88px;
    border-top: 4px solid var(--green);
    color: var(--green); font-weight: 900; font-size: 38px;
    line-height: 40px; text-align: right; padding-top: 2px;
  }
  .product-type {
    position: absolute; left: 0; width: 1100px; top: 626px;
    text-align: center; padding-left: 30px;
    color: var(--green); font-weight: 600; font-size: 30px; letter-spacing: 1px;
  }
  .benefit {
    position: absolute; top: 678px; width: 260px;
    text-align: center;
  }
  .benefit-icon { display: block; margin: 0 auto; }
  .benefit-text {
    margin-top: 24px;
    color: var(--white); font-weight: 700; font-size: 24px;
  }
  .benefit-energy { left: 193px; }
  .benefit-focus { left: 492px; }
  .benefit-endurance { left: 790px; }
</style>
</head>
<body>
<div class="label">
  <svg class="label-shapes" width="1100" height="984" viewBox="0 0 1100 984">
    <defs>
      <linearGradient id="silver" x1="0" y1="0" x2="1" y2="0.4">
        <stop offset="0" stop-color="var(--silver-dark)"/>
        <stop offset="0.45" stop-color="var(--silver-light)"/>
        <stop offset="1" stop-color="var(--silver-mid)"/>
      </linearGradient>
    </defs>
    <rect width="1100" height="984" fill="url(#silver)"/>
    <rect y="10" width="1100" height="12" fill="var(--lime)"/>
    <rect y="22" width="1100" height="15" fill="var(--green)"/>
    <polygon points="0,37 171,37 48,744 0,744" fill="var(--green)"/>
    <polygon points="171,37 219,37 88,744 48,744" fill="var(--charcoal)"/>
    <rect y="744" width="1100" height="216" fill="var(--green)"/>
    <rect y="958" width="1100" height="12" fill="var(--lime)"/>
    <rect y="970" width="1100" height="14" fill="var(--green-deep)"/>
  </svg>

  <div class="brand-mark">KL</div>
  <div class="claims-note">NO APPROVED THERAPEUTIC CLAIMS</div>

  <svg class="hero-art" viewBox="0 0 560 400" role="img" aria-label="Illustration of a sprinting runner dissolving into green particles with flowing light-green wave lines">
    <defs>
      <radialGradient id="heroGlow" cx="0.6" cy="0.55" r="0.55">
        <stop offset="0" stop-color="var(--lime)" stop-opacity="0.55"/>
        <stop offset="1" stop-color="var(--lime)" stop-opacity="0"/>
      </radialGradient>
    </defs>
    <rect width="560" height="400" fill="url(#heroGlow)"/>
  </svg>

  <div class="spec-line spec-banned">ZERO BANNED SUBSTANCES</div>
  <div class="spec-line spec-weight">Net weight<b>594 LBS (270g)</b></div>

  <div class="product-name">KESTRO</div>
  <div class="product-variant">SURGE<br>UP</div>
  <div class="product-type">DIETARY SUPPLEMENT</div>

  <div class="benefit benefit-energy">
    <svg class="benefit-icon" width="176" height="176" viewBox="0 0 176 176">
      <circle cx="88" cy="88" r="86" fill="var(--silver-light)" stroke="var(--lime-soft)" stroke-width="2"/>
      <circle cx="88" cy="88" r="70" fill="var(--lime)"/>
      <path d="M58 112 A38 38 0 1 1 118 112" fill="none" stroke="var(--white)" stroke-width="7" stroke-linecap="round"/>
      <line x1="88" y1="92" x2="106" y2="70" stroke="var(--white)" stroke-width="7" stroke-linecap="round"/>
      <circle cx="88" cy="92" r="6" fill="var(--white)"/>
      <line x1="76" y1="116" x2="100" y2="116" stroke="var(--white)" stroke-width="6" stroke-linecap="round"/>
    </svg>
    <div class="benefit-text">MILES OF ENERGY</div>
  </div>

  <div class="benefit benefit-focus">
    <svg class="benefit-icon" width="176" height="176" viewBox="0 0 176 176">
      <circle cx="88" cy="88" r="86" fill="var(--silver-light)" stroke="var(--lime-soft)" stroke-width="2"/>
      <circle cx="88" cy="88" r="70" fill="var(--lime)"/>
      <g fill="none" stroke="var(--white)" stroke-width="7" stroke-linecap="round" stroke-linejoin="round">
        <path d="M56 74 V58 H72"/>
        <path d="M104 58 H120 V74"/>
        <path d="M120 102 V118 H104"/>
        <path d="M72 118 H56 V102"/>
        <circle cx="88" cy="88" r="12"/>
      </g>
    </svg>
    <div class="benefit-text">FOCUS</div>
  </div>

  <div class="benefit benefit-endurance">
    <svg class="benefit-icon" width="176" height="176" viewBox="0 0 176 176" role="img" aria-label="Running figure icon">
      <circle cx="88" cy="88" r="86" fill="var(--silver-light)" stroke="var(--lime-soft)" stroke-width="2"/>
      <circle cx="88" cy="88" r="70" fill="var(--lime)"/>
    </svg>
    <div class="benefit-text">ENDURANCE</div>
  </div>
</div>
</body>
</html>
```